We invest in Electric Vehicles and renewable energy - help sell us!

INTRO: We want a PowerPoint template / Master Presentation to be used to sell our company and first investment fund to professional investors and to present ourselves to businesses that will develop the infrastructure projects in which we will invest.

WHO WE ARE: We are a newly created investment advisory and fund management company specialised in sustainable mobility.

WHAT WE DO: We invest in infrastructure projects that provide electric vehicles, charging infrastructure (charging stations etc) and associated renewable energy generation services (eg solar panels on roof-tops and solar parks, wind energy). The users of the projects in which we invest are operators of vehicle fleets (taxis, buses, delivery, which may be for 2, 3 and 4 wheel vehicles from motorbikes through cars, vans, buses and trucks).

PURPOSE OF THE POWERPOINT: We are looking for a presentation (1) to sell our investment services to investors (to raise money) and (2) to present what we do to fleet operators and service providers who will develop the projects.

CONTENT: We need all of the usual front cover slide / content slide / intermediate divider-heading slide / slides that integrate the most common tables, charts and smart graphics / team slide / a variety of text slides / a testimonial slide / Example project slide / Final contact and Disclaimer text slide etc all customised to the design. We rely on your experience for providing the further standard formats and layouts that one might find in a high-quality financial sector corporate presentation deck.

VERSIONS: We want three versions of the slides where there are images (eg front and back covers, section breaks, testimonial slides..). The three could be themed eg (1) futuristic and/or abstract in the theme of our investment scope (2) Street themes with vehicles and people in developed and developing markets (3) a mix of aerial and land-based views of roads (4) more explicit around the types of infrastructure in which we invest (vehicles of different types, charging infrastructure, solar panels on industrial and commercial roof tops etc)

LOOK & FEEL: The presentation must be sleek, dynamic if sober, with a clean feel, it should project an image of clarity and confidence, but also elicit some emotional appeal (even if it is very subtle!) ... we are in the e-mobility sector after all! We have an existing logo (attached).

We have an existing website www.dorelmont.capital (one day it will need an upgrade too!) it may serve as inspiration / allow you better to understand our activities!

SOME PICS THAT WE LIKE: for inspiration only (NON exhaustive!):

• https://www.klipvane.com/video/stock/unrecognizable-highway-traffic-head-on-bgkbvhtcmjn19iqta
• https://www.klipvane.com/video/stock/new-york-city-streets-nt1vyz3
• https://www.klipvane.com/video/stock/4k-time-lapse-of-traffic-speeding-on-a-straight-section-of-highway-during-an-evening-rush-hour-ps1llt0
• https://www.klipvane.com/video/stock/cinematic-urban-aerial-time-lapse-of-city-infrastructure-including-freeways-interstates-roads-streets-with-traffic-at-rush-hour-during-the-evening-bzjhqhqfmjbhns0h9
• https://www.klipvane.com/video/stock/charging-of-electric-car-eco-energy-transport-and-power-supply-environmentally-conscious-transportation-vehicle-plugged-in-charger-terminal-in-the-city-4k-rsl8pukqmejqpaojnn
• https://www.klipvane.com/video/stock/drone-view-of-modern-vehicle-driving-on-road-near-ploughed-field-and-wind-turbine-in-countryside-rzwqrsqvdkg85gavm

FINALLY: note the attached 'slides to include' are additonal slides that we want to be well presented (see additional detail on Slide 1 of the file)

Target Market(s)

Institutional investors (pension funds, asset managers, family offices) & the dreamer in each of us!!

Industry/Entity Type

Financial services (B2B NOT B2C)

Font styles to use
Other font styles liked:
• Calibri but can consider alternatives

Requirements
Must have
• We need all of the usual front cover slide / content slide / intermediate divider-heading slide / slides that integrate the most common tables, charts and smart graphics / team slide / a variety of text slides / a testimonial slide / Example project slide / Final contact and Disclaimer text slide etc all customised to the design. We rely on your experience for providing the further standard formats and layouts that one might find in a high-quality financial sector corporate presentation deck
Nice to have
• Would like to see any other pages that are standard in your experience! Also would like to see one version of the slides with a summary section clearly marked for each slide (with space for text) which will serve for quick reading of the presentation for key points)

```html
<!DOCTYPE html>
<html lang="en">
<head>
<meta charset="utf-8">
<title>Dorelmont Capital – Presentation Template</title>
<link href="https://fonts.googleapis.com/css2?family=Roboto:wght@300;400;500;700&display=swap" rel="stylesheet">
<style>
:root{
  --green-dark:#3b5a1c;
  --green:#4c6e24;
  --green-mid:#5f8a2c;
  --green-soft:#8fb05a;
  --text:#444;
  --muted:#8a8a8a;
  --sdg-green:#4c9f38;
  --sdg-orange:#fd9d24;
  --sdg-green-2:#3f7e44;
  --bg:#ffffff;
}
*{margin:0;padding:0;box-sizing:border-box}
html,body{width:815px;height:1200px;overflow:hidden;background:var(--bg)}
body{position:relative;font-family:'Roboto',Arial,sans-serif;color:var(--text)}
.slide{position:absolute;width:302px;height:170px;background:#fff;overflow:hidden;box-shadow:0 4px 14px rgba(0,0,0,.18)}
.col-l{left:75px}.col-r{left:437px}
.row1{top:28px}.row2{top:222px}.row3{top:416px}.row4{top:609px}.row5{top:803px}.row6{top:997px}
.abs{position:absolute}
.logo{position:absolute;font-weight:500;color:var(--green);font-size:6px;white-space:nowrap}
.logo.light{color:#fff}
.title{position:absolute;font-weight:300;color:var(--green-dark);font-size:12px;line-height:1.15;white-space:nowrap}
.title b{font-weight:700}
.subtitle{position:absolute;font-size:4.4px;letter-spacing:.6px;color:#555}
.para{position:absolute;font-size:2.9px;line-height:1.55;color:#666;text-align:justify}
.foot{position:absolute;left:22px;bottom:6px;font-size:3px;color:#aaa}
.pnum{position:absolute;right:22px;bottom:6px;font-size:3px;color:#aaa}
.photo{position:absolute}
.icon-circle{position:absolute;width:26px;height:26px;border-radius:50%;background:var(--green-dark);display:flex;align-items:center;justify-content:center}
.icon-circle svg{width:14px;height:14px}
.item-title{position:absolute;font-size:4.2px;letter-spacing:.4px;color:var(--green-dark);font-weight:500}
.item-text{position:absolute;font-size:2.9px;line-height:1.55;color:#777;text-align:justify}

/* cover */
.cover{background:linear-gradient(160deg,#2c4a1c,#4f7a2a 60%,#6d8f33)}
.cover .logo{left:20px;top:99px;font-size:20px;font-weight:300}
.cover-tag{position:absolute;left:21px;top:131px;font-size:5px;color:#e8f0dc;width:150px;line-height:1.2}
.cover-desc{position:absolute;left:21px;top:144px;font-size:4.2px;color:#e8f0dc;width:150px;line-height:1.25}

/* toc */
.toc-title{left:150px;top:30px}
.toc-list{position:absolute;left:154px;top:52px;width:130px;list-style:none}
.toc-list li{display:flex;justify-content:space-between;font-size:4.4px;line-height:8.3px;color:var(--green-mid)}
.toc-list li span:last-child{color:#555}

/* sdg */
.sdg{position:absolute;left:222px;width:57px}

/* team */
.member{position:absolute;top:52px;width:80px;text-align:center}
.member .pic{width:48px;height:48px;margin:0 auto}
.member .name{margin-top:14px;font-size:4.6px;font-weight:700;color:#333}
.member .role{font-size:4px;letter-spacing:.6px;color:#555}
.member .bio{margin-top:3px;font-size:3px;line-height:1.6;color:#888}

.closing{background:linear-gradient(150deg,#7fa04c,#95b463 50%,#6f9140)}
.closing .logo{left:28px;top:108px;font-size:18px;font-weight:300}
.closing-sub{position:absolute;left:31px;top:142px;font-size:12px;font-weight:300;color:#fff}
.closing-sub b{font-weight:700}
ul.bullets{position:absolute;left:152px;top:57px;width:128px;font-size:2.9px;line-height:1.6;color:#666;padding-left:6px}
ul.bullets li{margin-bottom:4px;text-align:justify}
</style>
</head>
<body>

<!-- Cover -->
<section class="slide col-l row1 cover">
  <div class="photo" style="inset:0;background:linear-gradient(180deg,rgba(20,40,20,.5),rgba(120,150,60,.25))" role="img" aria-label="Night city skyline with light trails of highway traffic, green tinted"></div>
  <div class="logo light">Dorelmont Capital</div>
  <p class="cover-tag">PROJECT FINANCE TO SCALE ELECTRIC VEHICLES, GLOBALLY</p>
  <p class="cover-desc">Dorelmont Capital is an investment advisory and management company whose mission is to scale deployment of low-carbon road transport solutions</p>
</section>

<!-- Table of contents -->
<section class="slide col-r row1">
  <div class="photo" style="left:0;top:0;width:120px;height:170px;background:linear-gradient(170deg,#d9d3b0,#9fb8a8 45%,#5fa3a0 75%,#c9b040)" role="img" aria-label="Covered electric vehicle charging stations in sunlight"></div>
  <div class="logo" style="left:240px;top:15px">Dorelmont Capital</div>
  <h2 class="title toc-title">Table of <b>Contents</b></h2>
  <ul class="toc-list">
    <li><span>About Us</span><span>1</span></li>
    <li><span>Primary Department</span><span>2</span></li>
    <li><span>Mission And Vision</span><span>3</span></li>
    <li><span>Service &amp; Clients</span><span>4</span></li>
    <li><span>Service</span><span>5</span></li>
    <li><span>Text Layout</span><span>6</span></li>
    <li><span>Text Layout</span><span>7</span></li>
    <li><span>Infographic Chart</span><span>8</span></li>
    <li><span>Table Chart</span><span>9</span></li>
    <li><span>Table Chart</span><span>10</span></li>
    <li><span>Table Chart</span><span>11</span></li>
    <li><span>Contact</span><span>12</span></li>
  </ul>
  <span class="pnum">1</span>
</section>

<!-- Impact measurement -->
<section class="slide col-l row2">
  <div class="logo" style="left:24px;top:15px">Dorelmont Capital</div>
  <h2 class="title" style="left:23px;top:36px;font-size:11.5px">Impact <span style="font-weight:400">Measurement</span><br><span style="font-weight:400">and Reporting</span></h2>
  <p class="para" style="left:20px;top:72px;width:177px;font-size:3.5px;color:#333">Dorelmont Capital is committed to sound risk management, responsible operations and to furthering the Paris Objectives and SDGs. Private placements will incorporate impact metrics as appropriate. Managed funds will operate a Measuring, Reporting and Verifying (MRV) system for the climate and sustainable development impact of individual projects and on a portfolio level.</p>
  <div class="abs" style="left:20px;top:114px;width:22px;height:22px;border-radius:50%;border:4px solid var(--green-soft)"></div>
  <p class="para" style="left:48px;top:114px;width:56px;font-size:3.4px;text-align:left;line-height:1.3">Fund investment processes will be certified for alignment with the UN Sustainable development goals</p>
  <svg class="abs" style="left:117px;top:116px" width="20" height="18" viewBox="0 0 20 18"><g fill="#222"><rect x="1" y="9" width="3" height="9"/><rect x="6" y="6" width="3" height="12"/><rect x="11" y="8" width="3" height="10"/><rect x="16" y="4" width="3" height="14"/></g><polyline points="2,6 7,3 12,5 17,1" stroke="#222" stroke-width="1" fill="none"/></svg>
  <p class="para" style="left:143px;top:114px;width:56px;font-size:3.4px;text-align:left;line-height:1.3">Impact indicators will be established and reported on for projects and portfolios of future funds</p>
  <div class="sdg" style="top:0;height:56px;background:var(--sdg-green)"></div>
  <div class="sdg" style="top:56px;height:58px;background:var(--sdg-orange)"></div>
  <div class="sdg" style="top:114px;height:56px;background:var(--sdg-green-2)"></div>
  <span class="foot">dorelmont.capital</span>
  <span class="pnum" style="right:8px">2</span>
</section>

<!-- What we do (diagonal) -->
<section class="slide col-r row2">
  <svg class="abs" style="left:0;top:0" width="302" height="170" viewBox="0 0 302 170" role="img" aria-label="Wind turbines over a coastal landscape at sunset">
    <defs><linearGradient id="windSky" x1="0" y1="0" x2="0" y2="1"><stop offset="0" stop-color="#b9c3dc"/><stop offset=".55" stop-color="#d9c2b8"/><stop offset=".75" stop-color="#8a8f6a"/><stop offset="1" stop-color="#5b4a2c"/></linearGradient></defs>
    <polygon points="48,0 205,0 128,112 196,170 0,170 0,138" fill="url(#windSky)"/>
    <line x1="140" y1="0" x2="30" y2="170" stroke="#fff" stroke-width="3"/>
    <line x1="160" y1="0" x2="50" y2="170" stroke="#fff" stroke-width="2"/>
  </svg>
  <div class="logo" style="left:220px;top:13px;font-size:8px">Dorelmont Capital</div>
  <h2 class="title" style="left:163px;top:58px;font-size:13px;letter-spacing:.4px">What <b>We Do</b></h2>
  <p class="abs" style="left:163px;top:83px;width:105px;font-size:5.4px;line-height:1.15;color:#888;font-weight:300">To deliver climate mitigation, health and other SDG impacts at scale, through electrification of commercial vehicle fleets.</p>
  <span class="pnum">3</span>
</section>

<!-- About us -->
<section class="slide col-l row3">
  <h2 class="title" style="left:22px;top:18px">About <b>Us</b></h2>
  <p class="subtitle" style="left:22px;top:37px">Subtitle Text</p>
  <p class="para" style="left:22px;top:47px;width:140px">We structure and advise on project finance for electric fleets, charging networks and the renewable power that feeds them. Our team works with fleet operators, developers and lenders to bring bankable projects to market, measure their climate impact and report clearly to investors. Every project is screened for sound risk, responsible operations and long-term value for the communities it serves. We structure and advise on project finance for electric fleets, charging networks and the renewable power that feeds them. Our team works with fleet operators, developers and lenders to bring bankable projects to market, measure their climate impact and report clearly to investors. Every project is screened for sound risk, responsible operations and long-term value for the communities it serves.</p>
  <div class="abs" style="left:22px;top:122px;width:140px;height:.5px;background:#aaa"></div>
  <p class="para" style="left:22px;top:126px;width:140px;font-size:2.8px;text-align:left">Our pipeline spans buses, taxis, delivery vans and two- and three-wheel fleets in developed and emerging markets, each paired with charging and clean generation sized to real duty cycles.</p>
  <div class="photo" style="left:182px;top:0;width:120px;height:170px;background:linear-gradient(135deg,#9fb49c,#6c8a78 50%,#c9d2cc)" role="img" aria-label="Close-up of a white electric car plugged into a charger"></div>
  <div class="logo light" style="left:240px;top:14px">Dorelmont Capital</div>
  <span class="foot">dorelmont.capital</span>
</section>

<!-- Who we are -->
<section class="slide col-r row3">
  <div class="logo" style="left:240px;top:14px">Dorelmont Capital</div>
  <div class="photo" style="left:22px;top:31px;width:114px;height:107px;background:linear-gradient(120deg,#7f8f6a,#5b6e8a 45%,#b04a44 80%,#d9d9d9)" role="img" aria-label="Worker charging an electric bus at a street charging post"></div>
  <h2 class="title" style="left:155px;top:33px">Who <b>We Are</b></h2>
  <p class="subtitle" style="left:155px;top:52px">Subtitle Text</p>
  <p class="para" style="left:155px;top:63px;width:120px">We structure and advise on project finance for electric fleets, charging networks and the renewable power that feeds them. Our team works with fleet operators, developers and lenders to bring bankable projects to market, measure their climate impact and report clearly to investors. Every project is screened for sound risk, responsible operations and long-term value for the communities it serves. Our pipeline spans buses, taxis, delivery vans and two- and three-wheel fleets in developed and emerging markets, each paired with charging and clean generation sized to real duty cycles.</p>
  <span class="foot">dorelmont.capital</span>
  <span class="pnum">5</span>
</section>

<!-- What we do (banner) -->
<section class="slide col-l row4">
  <div class="photo" style="left:0;top:0;width:302px;height:85px;background:linear-gradient(180deg,#2f9ad8 0%,#5fb7e6 40%,#6aa84a 62%,#8a7f76 88%)" role="img" aria-label="Flat illustration of wind turbines, solar panels and electric cars and trucks at charging points"></div>
  <h2 class="title" style="left:22px;top:98px">What <b>We Do</b></h2>
  <p class="para" style="left:22px;top:118px;width:260px">We structure and advise on project finance for electric fleets, charging networks and the renewable power that feeds them. Our team works with fleet operators, developers and lenders to bring bankable projects to market, measure their climate impact and report clearly to investors. Every project is screened for sound risk, responsible operations and long-term value for the communities it serves. Our pipeline spans buses, taxis, delivery vans and two- and three-wheel fleets in developed and emerging markets, each paired with charging and clean generation sized to real duty cycles.</p>
  <span class="foot">dorelmont.capital</span>
  <span class="pnum">6</span>
</section>

<!-- Our mission -->
<section class="slide col-r row4">
  <div class="logo" style="left:240px;top:14px">Dorelmont Capital</div>
  <div class="photo" style="left:0;top:24px;width:132px;height:122px;background:linear-gradient(180deg,#c9a070 0%,#8a7f7a 30%,#3e4f5e 55%,#4a86a8 100%)" role="img" aria-label="Aerial view of a solar tower surrounded by circular mirror fields"></div>
  <h2 class="title" style="left:150px;top:26px">Our <b>Mission</b></h2>
  <p class="subtitle" style="left:150px;top:45px">Subtitle Text</p>
  <ul class="bullets">
    <li>Mobilise private capital for electric fleets and charging across growth markets, with clear and measurable climate outcomes.</li>
    <li>Pair every fleet with clean power, from rooftop solar on depots to larger solar and wind parks.</li>
    <li>Work alongside operators and developers from early design through construction, operation and refinancing of each project.</li>
    <li>Report impact with rigour, so investors see the tonnes avoided and the jobs and health gains delivered.</li>
  </ul>
  <span class="foot">dorelmont.capital</span>
  <span class="pnum">12</span>
</section>

<!-- Text and icons -->
<section class="slide col-l row5">
  <div class="logo" style="left:240px;top:14px">Dorelmont Capital</div>
  <h2 class="title" style="left:23px;top:18px">Text and icons<br><b>Creative Slide</b></h2>
  <p class="subtitle" style="left:23px;top:58px">Subtitle Text</p>
  <p class="para" style="left:23px;top:69px;width:120px">We structure and advise on project finance for electric fleets, charging networks and the renewable power that feeds them. Our team works with fleet operators, developers and lenders to bring bankable projects to market, measure their climate impact and report clearly to investors. Every project is screened for sound risk, responsible operations and long-term value for the communities it serves.</p>

  <div class="icon-circle" style="left:164px;top:31px"><svg viewBox="0 0 14 14"><rect x="1" y="3" width="12" height="7" fill="none" stroke="#fff" stroke-width=".8"/><path d="M1 6.5h12M5 3v7M9 3v7M7 10v3" stroke="#fff" stroke-width=".6"/></svg></div>
  <p class="item-title" style="left:198px;top:31px">Your title goes here</p>
  <p class="item-text" style="left:198px;top:38px;width:82px">Short note on this service line and the value it brings to partners</p>

  <div class="icon-circle" style="left:164px;top:72px"><svg viewBox="0 0 14 14"><path d="M4 2v3M7 2v3M3 5h5v3a2.5 2.5 0 0 1-5 0zM5.5 10.5v2" stroke="#fff" stroke-width=".8" fill="none"/><path d="M9 11c0-3 2-5 4-5 0 3-2 5-4 5z" fill="none" stroke="#fff" stroke-width=".7"/></svg></div>
  <p class="item-title" style="left:198px;top:73px">Your title goes here</p>
  <p class="item-text" style="left:198px;top:80px;width:82px">Short note on this service line and the value it brings to partners</p>

  <div class="icon-circle" style="left:164px;top:114px"><svg viewBox="0 0 14 14"><path d="M7 6v7M7 6L7 1M7 6l4.5 2.5M7 6L2.5 8.5" stroke="#fff" stroke-width=".8" fill="none"/></svg></div>
  <p class="item-title" style="left:198px;top:116px">Your title goes here</p>
  <p class="item-text" style="left:198px;top:123px;width:82px">Short note on this service line and the value it brings to partners</p>
  <span class="foot">dorelmont.capital</span>
  <span class="pnum">7</span>
</section>

<!-- Your title slide -->
<section class="slide col-r row5">
  <div class="logo" style="left:240px;top:14px">Dorelmont Capital</div>
  <h2 class="title" style="left:22px;top:17px">Your title <b>slide here</b></h2>
  <p class="subtitle" style="left:22px;top:37px">Subtitle Text</p>
  <p class="para" style="left:22px;top:47px;width:260px">We structure and advise on project finance for electric fleets, charging networks and the renewable power that feeds them. Our team works with fleet operators, developers and lenders to bring bankable projects to market, measure their climate impact and report clearly to investors. Every project is screened for sound risk, responsible operations and long-term value for the communities it serves. Our pipeline spans buses, taxis, delivery vans and two- and three-wheel fleets in developed and emerging markets, each paired with charging and clean generation sized to real duty cycles.</p>

  <div class="icon-circle" style="left:23px;top:108px"><svg viewBox="0 0 14 14"><rect x="1" y="3" width="12" height="7" fill="none" stroke="#fff" stroke-width=".8"/><path d="M1 6.5h12M5 3v7M9 3v7M7 10v3" stroke="#fff" stroke-width=".6"/></svg></div>
  <p class="item-title" style="left:54px;top:109px">Your title here</p>
  <p class="item-text" style="left:54px;top:116px;width:38px;text-align:left">Short note on this point for partners</p>

  <div class="icon-circle" style="left:112px;top:108px"><svg viewBox="0 0 14 14"><circle cx="7" cy="7" r="2.5" fill="none" stroke="#fff" stroke-width=".8"/><path d="M7 1v2M7 11v2M1 7h2M11 7h2M2.8 2.8l1.4 1.4M9.8 9.8l1.4 1.4M2.8 11.2l1.4-1.4M9.8 4.2l1.4-1.4" stroke="#fff" stroke-width=".7"/></svg></div>
  <p class="item-title" style="left:143px;top:109px">Your title here</p>
  <p class="item-text" style="left:143px;top:116px;width:38px;text-align:left">Short note on this point for partners</p>

  <div class="icon-circle" style="left:200px;top:108px"><svg viewBox="0 0 14 14"><path d="M7 6v7M7 6L7 1M7 6l4.5 2.5M7 6L2.5 8.5" stroke="#fff" stroke-width=".8" fill="none"/></svg></div>
  <p class="item-title" style="left:231px;top:109px">Your title here</p>
  <p class="item-text" style="left:231px;top:116px;width:38px;text-align:left">Short note on this point for partners</p>
  <span class="foot">dorelmont.capital</span>
  <span class="pnum">9</span>
</section>

<!-- Team -->
<section class="slide col-l row6">
  <div class="logo" style="left:240px;top:14px">Dorelmont Capital</div>
  <h2 class="title" style="left:0;width:302px;text-align:center;top:16px">Team <b>Experts</b></h2>
  <p class="subtitle" style="left:0;width:302px;text-align:center;top:37px">Subtitle Text</p>
  <div class="member" style="left:30px">
    <div class="pic" style="background:linear-gradient(160deg,#3a3a3a,#7b7f86)" role="img" aria-label="Portrait photo of the CEO"></div>
    <p class="name">Jhon Doe</p><p class="role">CEO</p>
    <p class="bio">A short note on background<br>and focus area</p>
  </div>
  <div class="member" style="left:111px">
    <div class="pic" style="background:linear-gradient(180deg,#4a6fa0,#8a7f80 55%,#3b3030)" role="img" aria-label="Portrait photo of the CTO"></div>
    <p class="name">Jhon Doe</p><p class="role">CTO</p>
    <p class="bio">A short note on background<br>and focus area</p>
  </div>
  <div class="member" style="left:192px">
    <div class="pic" style="background:linear-gradient(160deg,#2e3a2c,#6b5a4a)" role="img" aria-label="Portrait photo of the Director"></div>
    <p class="name">Jhon Doe</p><p class="role">Director</p>
    <p class="bio">A short note on background<br>and focus area</p>
  </div>
  <span class="foot">dorelmont.capital</span>
  <span class="pnum">10</span>
</section>

<!-- Closing -->
<section class="slide col-r row6 closing">
  <div class="photo" style="inset:0;background:linear-gradient(180deg,rgba(90,130,50,.3),rgba(160,190,110,.35))" role="img" aria-label="Zero-emission hydrogen bus on a tree-lined road, green tinted"></div>
  <div class="logo light">Dorelmont Capital</div>
  <p class="closing-sub">Vision &amp; <b>Mission</b></p>
</section>

</body>
</html>
```